Construction Site Sign

4' high x 8' wide construction site sign using the attached logo (small correction required) Utilize the red, white and blue colors; add the company address, telephone numbers and website.

58 Fenwick Mill Road, Suite 4
Crawford, Georgia 30630
(706) 318-2946 Office
(706) 561-3082 Fax
www.hollowbrookbuilders.biz

```html
<!DOCTYPE html>
<html lang="en">
<head>
<meta charset="utf-8">
<title>Hollowbrook Builders – Site Sign</title>
<link rel="stylesheet" href="https://fonts.googleapis.com/css2?family=Jost:wght@400;600;700&display=swap">
<style>
  :root {
    --backdrop: #7a7170;
    --sign-white: #ffffff;
    --brand-blue: #1257a6;
    --chevron-grey: #a7a9ac;
    --text-white: #ffffff;
  }
  * { margin: 0; padding: 0; box-sizing: border-box; }
  html, body {
    width: 1200px; height: 720px; overflow: hidden;
    background: var(--backdrop);
  }
  .sign {
    position: absolute; left: 112px; top: 116px;
    width: 976px; height: 488px;
    background: var(--sign-white);
    overflow: hidden;
    font-family: "Jost", sans-serif;
  }
  .sign-panels { position: absolute; inset: 0; }
  .panel-blue { fill: var(--brand-blue); }
  .panel-chevron { fill: var(--chevron-grey); }

  .brand-name {
    position: absolute; left: 40px; top: 176px; width: 430px;
    text-align: center;
    color: var(--brand-blue);
    font-weight: 700; font-size: 54px; line-height: 1.05;
    letter-spacing: 1px; text-transform: uppercase;
  }

  .address {
    position: absolute; right: 36px; top: 46px;
    text-align: right; color: var(--text-white);
    font-weight: 400; font-size: 33px; line-height: 44px;
    font-style: normal;
  }
  .contact-lines {
    position: absolute; right: 38px; top: 310px;
    color: var(--text-white);
  }
  .contact-line {
    display: flex; align-items: center; justify-content: flex-end;
    gap: 6px; font-weight: 600; font-size: 34px; line-height: 50px;
    letter-spacing: 0.5px;
  }
  .contact-icon { width: 40px; height: 36px; fill: var(--text-white); }
  .website {
    position: absolute; right: 22px; top: 420px;
    color: var(--text-white); font-weight: 600; font-size: 29px;
  }
</style>
</head>
<body>
  <div class="sign">
    <svg class="sign-panels" viewBox="0 0 976 488" width="976" height="488" aria-hidden="true">
      <polygon class="panel-chevron" points="420,0 448,0 610,244 493,488 465,488 582,244"/>
      <polygon class="panel-blue" points="448,0 976,0 976,488 493,488 610,244"/>
    </svg>

    <div class="brand-name">Hollowbrook<br>Builders</div>

    <address class="address">
      58 Fenwick Mill Road,<br>
      Suite 4 Crawford,<br>
      Georgia 30630
    </address>

    <div class="contact-lines">
      <div class="contact-line">
        <svg class="contact-icon" viewBox="0 0 40 36" aria-label="Office phone">
          <path d="M2 12c0-6 8-9 18-9s18 3 18 9v3h-9v-4c-3-1-15-1-18 0v4H2z"/>
          <path d="M9 17h22l5 16H4z"/>
        </svg>
        <span>(706) 318-2946</span>
      </div>
      <div class="contact-line">
        <svg class="contact-icon" viewBox="0 0 40 36" aria-label="Fax">
          <rect x="10" y="1" width="20" height="10"/>
          <path d="M3 12h34a2 2 0 0 1 2 2v14H1V14a2 2 0 0 1 2-2z"/>
          <rect x="9" y="22" width="22" height="13" fill="#1257a6"/>
          <rect x="11" y="24" width="18" height="11"/>
        </svg>
        <span>(706) 561-3082</span>
      </div>
    </div>

    <div class="website">www.hollowbrookbuilders.biz</div>
  </div>
</body>
</html>
```